Business Card for a Dental Office

The design should communicate integrity, quality and reliability. We also want the card look elegant, simple, but still stand out, different from the traditional-dental-office business card.

Business

```html
<!DOCTYPE html>
<html lang="en">
<head>
<meta charset="utf-8">
<title>Harwick Dental Studio – Business Card</title>
<link href="https://fonts.googleapis.com/css2?family=Roboto+Condensed:wght@300;400;700&display=swap" rel="stylesheet">
<style>
  :root{
    --page:#d9d9db;
    --navy-deep:#0b2765;
    --navy:#17409a;
    --royal:#2c64c4;
    --gold:#e5b90f;
    --ink:#111111;
    --grey:#555555;
    --paper:#ffffff;
    --icon:#1d4fa3;
  }
  *{box-sizing:border-box;margin:0;padding:0}
  html,body{width:1200px;height:960px;overflow:hidden}
  body{
    background:radial-gradient(ellipse at 50% 45%, #f1f1f2 0%, var(--page) 60%, #bdbdc0 100%);
    font-family:"Roboto Condensed", Arial, sans-serif;
    position:relative;
  }
  .card{
    position:absolute;
    width:560px;height:320px;
    border-radius:4px;
    box-shadow:0 18px 40px rgba(0,0,0,.25), 0 2px 6px rgba(0,0,0,.15);
    overflow:hidden;
  }
  /* Front */
  .card--front{
    left:90px;top:110px;
    background:radial-gradient(ellipse at 55% 45%, var(--royal) 0%, var(--navy) 45%, var(--navy-deep) 100%);
    display:flex;flex-direction:column;align-items:center;justify-content:center;
  }
  .brand{display:flex;align-items:center;gap:14px}
  .brand__mark{width:30px;height:30px;background:var(--gold);flex:none}
  .brand__name{
    font-weight:700;text-transform:uppercase;letter-spacing:.5px;line-height:1;
    white-space:nowrap;
  }
  .card--front .brand__name{color:#fff;font-size:40px}
  .tagline{
    color:var(--gold);font-weight:400;text-transform:uppercase;
    letter-spacing:.3px;line-height:1;white-space:nowrap;
  }
  .card--front .tagline{font-size:20px;margin-top:12px}

  /* Back */
  .card--back{
    left:550px;top:530px;
    background:var(--paper);
    padding:30px 34px;
  }
  .card--back .brand__mark{width:22px;height:22px}
  .card--back .brand__name{color:var(--ink);font-size:30px}
  .card--back .tagline{font-size:15px;margin-top:6px;margin-left:36px}
  .person{margin-top:26px}
  .person__name{font-size:27px;font-weight:700;color:var(--ink);line-height:1}
  .person__title{font-size:17px;font-weight:300;color:var(--grey);margin-top:4px}
  .card__body{display:flex;justify-content:space-between;margin-top:16px}
  .services{list-style:none;font-size:16px;color:var(--ink);line-height:1.35}
  .services li::before{content:"• "}
  .contacts{list-style:none;font-size:16px;color:var(--ink);margin-top:10px}
  .contacts li{display:flex;align-items:center;gap:10px;height:28px}
  .contacts svg{width:22px;height:22px;flex:none}
</style>
</head>
<body>

<section class="card card--front" aria-label="Card front">
  <div class="brand">
    <span class="brand__mark"></span>
    <span class="brand__name">Harwick Dental Studio</span>
  </div>
  <p class="tagline">Gentle care for a smile worth sharing</p>
</section>

<section class="card card--back" aria-label="Card back">
  <div class="brand">
    <span class="brand__mark"></span>
    <span class="brand__name">Harwick Dental Studio</span>
  </div>
  <p class="tagline">Gentle care for a smile worth sharing</p>

  <div class="person">
    <p class="person__name">Your Name Here</p>
    <p class="person__title">Chief Executive Officer</p>
  </div>

  <div class="card__body">
    <ul class="services">
      <li>General Dentistry</li>
      <li>Cosmetic Dentistry</li>
      <li>Beautiful Dentures</li>
      <li>Sedation Dentistry</li>
    </ul>
    <ul class="contacts">
      <li>
        <svg viewBox="0 0 22 22" aria-hidden="true"><circle cx="11" cy="11" r="11" fill="var(--icon)"/><rect x="7.5" y="5" width="7" height="12" rx="1.2" fill="none" stroke="#fff" stroke-width="1.4"/><circle cx="11" cy="15" r=".8" fill="#fff"/></svg>
        (222) 123-4567
      </li>
      <li>
        <svg viewBox="0 0 22 22" aria-hidden="true"><circle cx="11" cy="11" r="11" fill="var(--icon)"/><path d="M7 6c1-1 2 0 2.5 1.2s0 1.6-.6 2c.6 1.4 1.5 2.4 2.9 3 .4-.6.9-1.1 2-.6S15 13 14 14c-1.5 1.5-8.5-4.5-7-8z" fill="#fff"/></svg>
        (222) 123-4567
      </li>
      <li>
        <svg viewBox="0 0 22 22" aria-hidden="true"><circle cx="11" cy="11" r="11" fill="var(--icon)"/><rect x="5.5" y="7" width="11" height="8" fill="#fff"/><path d="M5.5 7l5.5 4.5L16.5 7" fill="none" stroke="var(--icon)" stroke-width="1.2"/></svg>
        name@email.com
      </li>
      <li>
        <svg viewBox="0 0 22 22" aria-hidden="true"><circle cx="11" cy="11" r="11" fill="var(--icon)"/><g fill="none" stroke="#fff" stroke-width="1.1"><circle cx="11" cy="11" r="5.5"/><ellipse cx="11" cy="11" rx="2.4" ry="5.5"/><path d="M5.5 11h11M6.5 8h9M6.5 14h9"/></g></svg>
        www.yourdomain.com
      </li>
    </ul>
  </div>
</section>

</body>
</html>
```